Design a modern, classy & professional business card for an online real estate agency, specializing in medium-luxury properties in Thailand and later in Singapore and UK.

Possible design ideas so far: (not essential)

- curved corner(s) to the card, white on front & turquoise on back or visa versa.

- front of card - clear and simple, company name in metallic grey/monochrome, logo graphic & company name on front in spot UV or embossed/debossed effect.

- back of card - large, close-cropped, 'ghost' patterns of the C-shaped curves of logo, or company name repeated on back of card in spot UV.

Target Market(s)

- young to middle-aged professionals mainly (but ideally should design should suit all)

- UK, US,EU,AUS & ASIAN mainly (but ideally should design should suit all countries)

Industry/Entity Type

Real Estate

Requirements
Must have
• THEME:
- Luxurious & Modern
- Clean & striking
- Unique & creative

INFO:
- Logo & company name on front
- Contact details on back:

Tobias Lindqvist
Managing Director

www.velmoraestates.example
www.velmoraestates-uk.example

Tel: 083-274-6190
email: tobias@velmoraestates.example

(contact details can be displayed in any order as suites design.)

Nice to have
• - curved corner(s) to the card, white on front & turquoise on back or visa versa.

Should not have
• - No generic images of properties, palm trees/coconut trees etc.

- No other other bold colors, except for main turquoise, grey, metallic white & black theme.

- No obvious business card templates

```html
<!DOCTYPE html>
<html lang="en">
<head>
<meta charset="utf-8">
<title>Velmora Estates — Business Card</title>
<link rel="stylesheet" href="https://fonts.googleapis.com/css2?family=Open+Sans:wght@400;600;700&display=swap">
<style>
  :root {
    --stage: #e9ebec;
    --card-white: #ffffff;
    --teal: #2ab3ae;
    --teal-deep: #1f9a96;
    --teal-light: #5fd3cf;
    --ink-grey: #6f7476;
    --ink-soft: #9aa0a2;
    --shadow: rgba(30, 40, 45, 0.18);
  }
  * { box-sizing: border-box; margin: 0; padding: 0; }
  html, body {
    width: 1200px;
    height: 2400px;
    overflow: hidden;
    background: var(--stage);
    font-family: "Open Sans", Arial, sans-serif;
  }
  .variant {
    height: 800px;
    display: flex;
    align-items: center;
    justify-content: center;
    gap: 40px;
  }
  .card {
    position: relative;
    width: 540px;
    height: 310px;
    border-radius: 22px;
    box-shadow: 0 10px 28px var(--shadow);
    overflow: hidden;
  }
  .card-front { background: var(--card-white); }
  .card-back {
    background:
      radial-gradient(circle at 75% 80%, var(--teal-light) 0%, transparent 45%),
      linear-gradient(135deg, var(--teal-deep) 0%, var(--teal) 55%, var(--teal-light) 100%);
  }
  .brand {
    position: absolute;
    display: flex;
    align-items: center;
    gap: 10px;
  }
  .brand-mark {
    width: 32px;
    height: 32px;
    background: var(--teal);
  }
  .brand-name {
    font-size: 22px;
    font-weight: 600;
    color: var(--ink-grey);
    letter-spacing: 0.2px;
  }
  .contact-list {
    position: absolute;
    list-style: none;
    font-size: 11.5px;
    line-height: 20px;
    color: var(--ink-grey);
  }
  .contact-list li { display: flex; align-items: center; gap: 7px; }
  .contact-list svg { width: 10px; height: 10px; fill: var(--teal); flex: none; }
  .person { position: absolute; }
  .person-name {
    font-size: 15px;
    font-weight: 700;
    color: var(--teal);
  }
  .person-title {
    font-size: 11px;
    color: var(--ink-soft);
    margin-top: 2px;
  }
  .align-right { text-align: right; }
  .social-row {
    position: absolute;
    right: 34px;
    bottom: 30px;
    display: flex;
    gap: 6px;
  }
  .social-row span {
    width: 13px;
    height: 13px;
    background: var(--teal);
    border-radius: 2px;
  }
</style>
</head>
<body>

<svg width="0" height="0" style="position:absolute">
  <symbol id="icon-phone" viewBox="0 0 10 10"><path d="M2 0.5 L3.6 2.6 L2.7 3.6 Q4 6 6.4 7.3 L7.4 6.4 L9.5 8 L8.4 9.5 Q3.5 9 0.5 1.6 Z"/></symbol>
  <symbol id="icon-mail" viewBox="0 0 10 10"><path d="M0.5 2 H9.5 V8 H0.5 Z M1.2 2.6 L5 5.4 L8.8 2.6" /></symbol>
  <symbol id="icon-globe" viewBox="0 0 10 10"><circle cx="5" cy="5" r="4.5"/></symbol>
</svg>

<!-- Variant one -->
<section class="variant">
  <article class="card card-front">
    <div class="brand" style="left:34px; top:30px;">
      <span class="brand-mark"></span>
      <span class="brand-name">Velmora Estates</span>
    </div>
    <ul class="contact-list" style="left:34px; top:82px;">
      <li><svg><use href="#icon-phone"/></svg>083-274-6190</li>
      <li><svg><use href="#icon-mail"/></svg>tobias@velmoraestates.example</li>
      <li><svg><use href="#icon-globe"/></svg>www.velmoraestates.example</li>
      <li><svg><use href="#icon-globe"/></svg>www.velmoraestates-uk.example</li>
    </ul>
    <div class="person align-right" style="right:34px; top:140px;">
      <p class="person-name">Tobias Lindqvist</p>
      <p class="person-title">Managing Director</p>
    </div>
    <div class="social-row"><span></span><span></span><span></span></div>
  </article>
  <article class="card card-back" role="img" aria-label="Ghost pattern of interlocking rings in spot UV on turquoise"></article>
</section>

<!-- Variant two -->
<section class="variant">
  <article class="card card-front">
    <div class="brand" style="left:34px; top:30px;">
      <span class="brand-mark"></span>
      <span class="brand-name">Velmora Estates</span>
    </div>
    <ul class="contact-list" style="left:34px; top:82px;">
      <li><svg><use href="#icon-phone"/></svg>083-274-6190</li>
      <li><svg><use href="#icon-mail"/></svg>tobias@velmoraestates.example</li>
    </ul>
    <ul class="contact-list" style="left:34px; bottom:30px;">
      <li><svg><use href="#icon-globe"/></svg>www.velmoraestates.example</li>
      <li><svg><use href="#icon-globe"/></svg>www.velmoraestates-uk.example</li>
    </ul>
    <div class="person align-right" style="right:34px; top:140px;">
      <p class="person-name">Tobias Lindqvist</p>
      <p class="person-title">Managing Director</p>
    </div>
    <div class="social-row"><span></span><span></span><span></span></div>
  </article>
  <article class="card card-back" role="img" aria-label="Ghost pattern of interlocking rings in spot UV on turquoise"></article>
</section>

<!-- Variant three -->
<section class="variant">
  <article class="card card-front">
    <div class="person" style="left:34px; top:30px;">
      <p class="person-name">Tobias Lindqvist</p>
      <p class="person-title">Managing Director</p>
    </div>
    <ul class="contact-list" style="left:34px; top:82px;">
      <li><svg><use href="#icon-phone"/></svg>083-274-6190</li>
      <li><svg><use href="#icon-mail"/></svg>tobias@velmoraestates.example</li>
      <li><svg><use href="#icon-globe"/></svg>www.velmoraestates.example</li>
      <li><svg><use href="#icon-globe"/></svg>www.velmoraestates-uk.example</li>
    </ul>
    <div class="brand" style="right:34px; top:138px;">
      <span class="brand-mark"></span>
      <span class="brand-name">Velmora Estates</span>
    </div>
    <div class="social-row"><span></span><span></span><span></span></div>
  </article>
  <article class="card card-back" role="img" aria-label="Ghost pattern of interlocking rings in spot UV on turquoise"></article>
</section>

</body>
</html>
```